Eye Surgeon Need Book Cover For "Guarding Your Inner Sight" book
A Handbook On Ocular Disorders, Therapies & Selecting An Eye Expert
Brief Overview:
I am an International Retina Surgeon. I am developing dedicated eye surgery centers in Saratoga Springs, New York, in Amman, Jordan and in Dubai, UAE. In my private practice in Saratoga Springs, New York, I have found that patients are scared of losing their vision and are looking for clear answers they can understand. I wrote this book to help patients get those clear answers to understanding their symptoms and treatment plan for retinal diseases like Age-Related Macular Degeneration and Retinal Detachment.
Brand:
Dr. Selim Kourani (Dr. Lex)
Medical
My target audience is people who have been diagnosed with a retinal condition like Age-Related Macular Degeneration and are looking for expert help. It is also new patients locally that have been referred to me by another physician. My audience is generally age 55 and older with vision problems.
I require a front and back cover (5-1/2 inches by 8-1/2 inches) plus a narrow spine for my 100-page SOFT-COVER book. The title is “Guarding Your Inner Sight”. The Sub-Title is “A Handbook On Ocular Disorders, Therapies & Selecting An Eye Expert”. The Author is Selim R. Kourani, MD, MBA
There must be a starburst or some other noticeable announcement on the front cover “More Free Resources at www.BrookvaleOcular.com”
You will need to leave space on the back cover to insert an ISBM. You will insert my photo (on the back cover next to the author bio) and you can choose which one you like, how big it is and where to place it.
Author Bio: Dr. Selim Kourani is the owner of Pinecrest Macula & Vision Ophthalmology, CEO of The Halvern Ocular Surgical Center and Clinical Assistant Professor of Ophthalmology at Corbell Medical College. He has made his home in beautiful Saratoga Springs, NY with his wife Wendy.
The cover needs to be serious and give the impression it was written for someone older with vision problems. I have included images of vision loss that a person may be experiencing. The font needs to be large print as our audience has vision problems.
The price is $16.95 and the words “First Printing” need to be on the back cover.
The spine is the standard stuff on a spine.
Use this copy for the back cover.
Back Cover Copy: Through the years, I feel that I have learned more from my dear patients than I could possibly give to them. This book is a way for me to make it easier for others to get the treatment and care they deserve as our vision allows us to maintain our quality of life. I put this book together for others to overcome their fears and get treatment early. If this book provides one bit of information that give you peace of mind with regard to any aspect of your eye health, then it will be wildly successful.
Image of Dr. Kourani for back cover
Image showing how someone with age related macular degeneration see.
Amsler Grid as seen by a normal, healthy eye.
Amsler grid as seem by someone with Age Related Macular Degeneration.

```html
<!DOCTYPE html>
<html lang="en">
<head>
<meta charset="utf-8">
<title>Guarding Your Inner Sight – Cover</title>
<link rel="stylesheet" href="https://fonts.googleapis.com/css2?family=Alfa+Slab+One&family=PT+Serif:wght@700&family=Roboto+Condensed:wght@700;900&display=swap">
<style>
  :root {
    --slate: #56617f;
    --slate-dark: #48536f;
    --tan: #c8a36a;
    --gold: #eab63f;
    --pale-gold: #f1d27a;
    --ink: #2a2622;
    --white: #ffffff;
    --purple: #6a3fa0;
    --blue-band: #4a63b8;
  }
  * { margin: 0; padding: 0; box-sizing: border-box; }
  html, body { width: 1200px; height: 904px; overflow: hidden; background: var(--slate); }
  .cover { position: relative; width: 1200px; height: 904px; overflow: hidden; background: var(--slate); font-family: "Roboto Condensed", Arial, sans-serif; }
  .abs { position: absolute; }

  /* Back cover */
  .bio-panel { left: 0; top: 0; width: 570px; height: 380px; background: var(--tan); }
  .bio-heading { left: 0; top: 14px; width: 570px; text-align: center; font-weight: 900; font-size: 30px; color: var(--ink); letter-spacing: 1px; }
  .bio-block { left: 44px; top: 72px; width: 514px; font-weight: 700; font-size: 20px; line-height: 28px; color: var(--ink); text-align: justify; }
  .author-figure { float: left; width: 112px; margin: 4px 14px 4px 0; }
  .author-photo { width: 98px; height: 128px; margin: 0 auto; background: linear-gradient(180deg, #b9c3cf, #5a6070); }
  .photo-caption { margin-top: 3px; text-align: center; font-weight: 900; font-size: 9px; line-height: 10px; color: var(--ink); }

  .quote-mark { font-family: "Alfa Slab One", Georgia, serif; color: var(--gold); font-size: 150px; line-height: 1; }
  .quote-open { left: 18px; top: 430px; }
  .quote-close { left: 462px; top: 748px; }
  .back-copy { left: 112px; top: 452px; width: 345px; font-weight: 700; font-size: 17px; line-height: 26px; color: var(--white); text-align: justify; }

  .isbn-box { left: 20px; top: 798px; width: 115px; height: 98px; background: var(--white); }
  .isbn-label { left: 24px; top: 800px; font-size: 9px; font-weight: 700; color: var(--ink); }
  .price { left: 20px; top: 858px; width: 115px; text-align: center; font-weight: 900; font-size: 28px; color: var(--ink); }
  .printing-badge { left: 150px; top: 800px; width: 96px; height: 96px; background: var(--blue-band); overflow: hidden; }
  .printing-first { left: 0; top: 2px; width: 96px; text-align: center; font-weight: 900; font-size: 38px; color: var(--pale-gold); }
  .printing-word { left: 0; top: 58px; width: 96px; height: 38px; background: var(--purple); text-align: center; font-weight: 900; font-size: 20px; line-height: 38px; color: var(--white); }
  .resources-band { left: 246px; top: 808px; width: 324px; height: 88px; background: linear-gradient(90deg, var(--purple), var(--blue-band)); color: var(--white); font-weight: 700; font-size: 24px; line-height: 30px; padding: 14px 0 0 14px; }

  /* Spine */
  .spine { left: 570px; top: 0; width: 67px; height: 904px; background: var(--slate-dark); }
  .spine-author { left: 592px; top: 20px; height: 270px; writing-mode: vertical-rl; font-weight: 900; font-size: 15px; color: var(--gold); letter-spacing: 1px; white-space: nowrap; }
  .spine-title { left: 583px; top: 300px; height: 590px; writing-mode: vertical-rl; font-weight: 900; font-size: 36px; color: var(--white); letter-spacing: 1px; white-space: nowrap; }

  /* Front cover */
  .title { left: 637px; top: 48px; width: 563px; text-align: center; font-family: "Alfa Slab One", Georgia, serif; font-size: 60px; line-height: 66px; color: var(--white); text-transform: uppercase; }
  .subtitle { left: 660px; top: 318px; width: 517px; text-align: center; font-family: "PT Serif", Georgia, serif; font-weight: 700; font-size: 22px; line-height: 28px; color: var(--pale-gold); }
  .front-lower { left: 637px; top: 465px; width: 563px; height: 439px; background: var(--tan); }
  .front-resources { left: 637px; top: 476px; width: 563px; text-align: center; font-weight: 900; font-size: 19px; line-height: 24px; color: var(--slate-dark); }
  .eye-art { left: 833px; top: 515px; width: 245px; height: 245px; background: radial-gradient(ellipse at center, #8a7050 0%, #b8935e 55%, var(--tan) 75%); }
  .author-band { left: 735px; top: 779px; width: 465px; height: 78px; background: var(--slate); color: var(--white); text-align: center; padding-top: 6px; }
  .author-name { font-weight: 900; font-size: 34px; line-height: 40px; }
  .author-creds { font-weight: 700; font-size: 17px; line-height: 22px; }
</style>
</head>
<body>
<main class="cover">
  <section class="back-cover">
    <div class="abs bio-panel"></div>
    <h2 class="abs bio-heading">AUTHOR BIO:</h2>
    <div class="abs bio-block">
      <figure class="author-figure">
        <div class="author-photo" role="img" aria-label="Portrait photograph of the author"></div>
        <figcaption class="photo-caption">DR. SELIM KOURANI<br>M.D., M.B.A.</figcaption>
      </figure>
      Dr. Selim Kourani is the owner of Pinecrest Macula &amp; Vision Ophthalmology, CEO of The Halvern Ocular Surgical Center and Clinical Assistant Professor of Ophthalmology at Corbell Medical College. He has made his home in beautiful Saratoga Springs, NY with his wife Wendy.
    </div>

    <span class="abs quote-mark quote-open">&ldquo;</span>
    <p class="abs back-copy">Through the years, I feel that I have learned more from my dear patients than I could possibly give to them. This book is a way for me to make it easier for others to get the treatment and care they deserve as our vision allows us to maintain our quality of life. I put this book together for others to overcome their fears and get treatment early. If this book provides one bit of information that give you peace of mind with regard to any aspect of your eye health, then it will be wildly successful.</p>
    <span class="abs quote-mark quote-close">&rdquo;</span>

    <div class="abs isbn-box"></div>
    <span class="abs isbn-label">ISBN</span>
    <span class="abs price">$16.95</span>
    <div class="abs printing-badge">
      <span class="abs printing-first">First</span>
      <span class="abs printing-word">PRINTING</span>
    </div>
    <div class="abs resources-band">More Free Resources at<br>www.BrookvaleOcular.com</div>
  </section>

  <section class="spine-area">
    <div class="abs spine"></div>
    <span class="abs spine-author">-DR. SELIM KOURANI M.D., M.B.A.</span>
    <span class="abs spine-title">GUARDING YOUR INNER SIGHT</span>
  </section>

  <section class="front-cover">
    <h1 class="abs title">Guarding<br>Your<br>Inner<br>Sight</h1>
    <p class="abs subtitle">A Handbook On Ocular Disorders, Therapies &amp; Selecting An Eye Expert</p>
    <div class="abs front-lower"></div>
    <p class="abs front-resources">More Free Resources at www.BrookvaleOcular.com</p>
    <div class="abs eye-art" role="img" aria-label="Line illustration of a human eye"></div>
    <div class="abs author-band">
      <div class="author-name">Dr. Selim Kourani</div>
      <div class="author-creds">M.D., M.B.A.</div>
    </div>
  </section>
</main>
</body>
</html>
```